Business card design based on existing website

Please make a business card that is consistent with the look and feel of my new website: http://tellbury.com.sg. By going to the site, I think you'll have all you need in terms of the work I do and the colors I use.

I would like to ask the winner of this project to then do a separate project to design my stationery.

Target Market(s)

Heads of human resources, people wanting psychotherapy, and executives wanting coaching. (It's quite a mix!)

Industry/Entity Type

Psychology

Contact Information for Business Card

Email: ray5678@tellbury.com.sg
Website: http://tellbury.com.sg
Tel: +65 94706218

(I will not have a physical address on the card)

Font styles to use
Serif

Colors

Designer to choose colors to be used in the design.

Requirements
Must have
• On the Front
• ==========
• Have "Dr. Raymond Tellbury" using the font of the website.
• Also "Executive Coach, Psychotherapist, Leadership Professor"
• The back should mention
• ==================
• My degrees
• -------------
• "PhD Kelworth; Post Doc Drayfield". E.g., "Raymond Tellbury (PhD Kelworth; Post Doc Drayfield)" where the text between brackets was in smaller font.
• My work
• ----------
• "Executive coach, psychotherapist, and leadership professor"
• My job titles
• ---------------
• "Principal (Tellbury Consulting)
• Adjunct Professor (Lornvale Commerce University)
• Adjunct Associate Professor (Pemberly Institute of Letters)
• Coach & Supervisor (OKTRAV) '
• Options:
• 1) you can abbreviate Adjunct Professor to "Adj Prof" or "Adj Professor"; and "Adjunct Associate Professor" to "Adj Assoc Prof"
• 2) you abbreviate "Pemberly Institute of Letters" and "Lornvale Commerce University" to "PIL" and "LCU"
• 3) You can also combine the titles for PIL and LCU, e.g., "Adjunct faculty (PIL & LCU)
Nice to have
• Because I work with many Chinese people, it is sometimes helpful to have my family name, "Tellbury", in caps. In the past I have not used caps because it takes away from the aesthetic of the card. Only use caps if it looks good.
• The uploaded image of a "RT" is something that may be helpful. I am undecided.
• THANK YOU for helping me!
Should not have
• No photos. In my industry people consider it overselling.

```html
<!DOCTYPE html>
<html lang="en">
<head>
<meta charset="utf-8">
<title>Dr. Raymond Tellbury – Business Card</title>
<link rel="stylesheet" href="https://fonts.googleapis.com/css2?family=Cormorant+Garamond:wght@500;600&family=Raleway:wght@400&display=swap">
<style>
  :root {
    --forest-deep: #17281a;
    --forest-mid: #2a4530;
    --forest-tab: #2c5232;
    --forest-line: #3d7a44;
    --brand-ink: #1f3b24;
    --paper: #ffffff;
    --ink-light: #ffffff;
  }
  * { margin: 0; padding: 0; box-sizing: border-box; }
  html, body { width: 1200px; height: 686px; overflow: hidden; background: var(--paper); }
  .card {
    position: relative;
    width: 1200px;
    height: 686px;
    overflow: hidden;
    background: var(--paper);
  }
  .card-art { position: absolute; inset: 0; }
  .holder-name {
    position: absolute;
    left: 34px;
    top: 58px;
    font-family: "Cormorant Garamond", Georgia, serif;
    font-weight: 600;
    font-size: 50px;
    letter-spacing: 1.5px;
    color: var(--ink-light);
    text-transform: uppercase;
    white-space: nowrap;
  }
  .holder-roles {
    position: absolute;
    left: 34px;
    top: 146px;
    width: 760px;
    font-family: "Raleway", Arial, sans-serif;
    font-size: 33px;
    line-height: 48px;
    color: var(--ink-light);
  }
  .contact {
    position: absolute;
    left: 34px;
    font-family: "Raleway", Arial, sans-serif;
    font-size: 31px;
    color: var(--ink-light);
    white-space: nowrap;
  }
  .contact-email { top: 398px; }
  .contact-web { top: 494px; }
  .contact-phone { top: 586px; }
  .brand-name {
    position: absolute;
    left: 800px;
    top: 290px;
    width: 370px;
    text-align: center;
    font-family: "Cormorant Garamond", Georgia, serif;
    font-weight: 600;
    font-size: 92px;
    line-height: 1;
    color: var(--brand-ink);
    white-space: nowrap;
  }
</style>
</head>
<body>
<div class="card">
  <svg class="card-art" width="1200" height="686" viewBox="0 0 1200 686" xmlns="http://www.w3.org/2000/svg">
    <defs>
      <radialGradient id="panelGlow" cx="0.32" cy="0.35" r="0.7">
        <stop offset="0" stop-color="#2a4530"/>
        <stop offset="1" stop-color="#17281a"/>
      </radialGradient>
      <linearGradient id="ruleGlow" x1="0" x2="1">
        <stop offset="0" stop-color="#3d7a44" stop-opacity="0.15"/>
        <stop offset="0.6" stop-color="#3d7a44" stop-opacity="0.9"/>
        <stop offset="1" stop-color="#3d7a44" stop-opacity="0.6"/>
      </linearGradient>
    </defs>

    <polygon class="panel" points="0,0 907,0 557,686 0,686" fill="url(#panelGlow)"/>

    <rect class="contact-rule" x="0" y="459" width="676" height="4" fill="url(#ruleGlow)"/>
    <rect class="contact-rule" x="0" y="553" width="628" height="4" fill="url(#ruleGlow)"/>

    <polygon class="icon-tab" points="596,384 711,384 673,458 558,458" fill="#2c5232"/>
    <polygon class="icon-tab" points="547,480 662,480 625,552 510,552" fill="#2c5232"/>
    <polygon class="icon-tab" points="499,574 614,574 575,650 460,650" fill="#2c5232"/>

    <g class="icon-send" fill="#ffffff">
      <polygon points="612,423 662,402 645,444 634,430"/>
      <polygon points="634,430 662,402 628,440"/>
    </g>
    <g class="icon-web">
      <rect x="556" y="498" width="40" height="27" rx="2" fill="none" stroke="#ffffff" stroke-width="4"/>
      <rect x="572" y="525" width="8" height="7" fill="#ffffff"/>
      <rect x="564" y="532" width="24" height="4" fill="#ffffff"/>
    </g>
    <g class="icon-phone" fill="#ffffff">
      <path d="M508,600 q22,-14 44,0 l-3,7 h-8 l-2,-5 q-8,-3 -18,0 l-2,5 h-8 z"/>
      <path d="M515,612 h30 l6,18 h-42 z"/>
      <circle cx="530" cy="620" r="5" fill="#2c5232"/>
    </g>
  </svg>

  <h1 class="holder-name">Dr. Raymond Tellbury</h1>
  <p class="holder-roles">Executive Coach, Psychotherapist, Leadership Professor</p>
  <p class="contact contact-email">ray5678@tellbury.com.sg</p>
  <p class="contact contact-web">www.tellbury.com.sg</p>
  <p class="contact contact-phone">+65.9470.62.18</p>

  <div class="brand-name">Tellbury</div>
</div>
</body>
</html>
```